Web Site Redesign

We operate a data centre facility specialing in colocation and Fibre optic connectivity (i.e. point to point fibre services and internet over fibre).

We have an existing site located at www.corvanlink.example however this is very very tired and requires a redesign. We are looking for a fresh new design that will be appealing to potential customers.

The Company name is Corvan Lk and the primary corporate colour is bright red with secondary colours of white, grey and black. Specific bright red can be seen in attached company logo.

Website needs to be modern, clean and professional representing our premium colocation and fibre provider branding.

Our company slogan is : safe. secure. reliable

We will provide feedback regardless of the quality of the design to ensure a better outcome for all parties.

Please feel free to contact us if you have any questions.

# The designer can use placeholder images or feel free to use any/all or none of the attached images
# The designer can use sample filler text

Target Market(s)

Technical IT Professionals as well C level executives (i.e. CEO's, CIO).

Industry/Entity Type

Internet

Requirements
Must have
• clean design
Nice to have
• A sidebar with two sections. 1 for current promo and 1 for "Let us call you back/contact you"
Should not have
• Clutter

```html
<!DOCTYPE html>
<html lang="en">
<head>
<meta charset="utf-8">
<title>Corvan Lk – Data Centre</title>
<link href="https://fonts.googleapis.com/css2?family=Arimo:wght@400;700&family=Nunito:wght@900&display=swap" rel="stylesheet">
<style>
:root{
  --red:#e8201f;
  --red-light:#ff6a66;
  --red-dark:#c8100f;
  --ink:#1f1f1f;
  --grey:#6f757b;
  --grey-text:#8a9096;
  --panel:#eceef0;
  --line:#d9dcdf;
  --white:#ffffff;
  --dark:#2a2e32;
}
*{box-sizing:border-box;margin:0;padding:0}
html,body{width:1176px;height:1200px;overflow:hidden;background:var(--white);font-family:"Arimo",Arial,sans-serif;color:var(--ink)}
.page{position:relative;width:1176px;height:1200px;background:linear-gradient(#e6e8ea 0,#fff 40px)}
.abs{position:absolute}
.btn{position:absolute;display:flex;align-items:center;justify-content:center;color:#fff;font-weight:700;font-size:14px;border-radius:5px;background:linear-gradient(#ff6b63,var(--red) 55%,var(--red-dark));box-shadow:0 1px 2px rgba(0,0,0,.25)}
/* brand */
.brand{left:78px;top:0;width:242px;height:278px;background:#fff;border-radius:0 0 8px 8px;box-shadow:0 2px 8px rgba(0,0,0,.25);display:flex;flex-direction:column;align-items:center;justify-content:center;gap:18px;z-index:3}
.brand-mark{width:90px;height:90px;border-radius:50%;background:var(--red)}
.brand-name{font-size:40px;font-weight:400;color:var(--ink)}
/* nav */
.nav a{height:46px;width:144px;top:65px;font-size:17px;font-weight:400;border-radius:7px;text-decoration:none}
.nav .current{background:linear-gradient(#4a5055,var(--dark));color:#ff5550}
/* hero */
.hero{left:59px;top:125px;width:1059px;height:407px;border-radius:8px;overflow:hidden;background:radial-gradient(ellipse at 55% 45%,#b9b2ad 0,#6b6a6c 30%,#2a2c30 65%,#111 100%);box-shadow:0 3px 8px rgba(0,0,0,.3)}
.bubble{position:absolute;border-radius:50%;display:flex;align-items:center;color:#fff;font-weight:700}
.bubble.red{left:49px;top:194px;width:164px;height:164px;background:radial-gradient(circle at 45% 35%,#ff6b66,var(--red) 60%,#b80c0b);color:var(--ink);font-weight:400;font-size:27px;line-height:1.05;padding-left:6px;box-shadow:0 0 14px rgba(255,255,255,.5)}
.bubble.dark{background:radial-gradient(circle at 50% 40%,#2a2a2a,#0b0b0b);box-shadow:0 0 0 2px rgba(232,32,31,.55),0 0 16px rgba(232,32,31,.5)}
.sec{left:881px;top:35px;width:116px;height:116px;justify-content:center;font-size:19px}
.rel{left:807px;top:205px;width:164px;height:164px;font-size:23px;line-height:1.05;padding-left:14px}
/* features */
.feature{top:550px;width:348px;height:192px;border:1px solid var(--line);border-radius:6px;padding:4px;background:#fff}
.feature-art{position:relative;width:100%;height:100%;border-radius:4px;background:linear-gradient(135deg,#d4d6d8,#eef0f1 50%,#cfd2d4)}
.feature h2{position:absolute;left:0;right:0;font-family:"Nunito",Arial,sans-serif;font-weight:900;color:var(--red);font-size:24px;line-height:22px;text-align:center}
.feature p{position:absolute;left:20px;right:20px;font-size:14px;font-weight:700;line-height:19px;text-align:center;color:var(--ink)}
.feature .btn{left:107px;top:137px;width:124px;height:27px}
/* lower panel */
.panel{left:59px;top:751px;width:1059px;height:359px;background:var(--panel);border-radius:6px}
.panel-main{left:414px;top:760px;width:695px;height:350px;border-radius:8px 8px 0 0;background:linear-gradient(#fff 0,#fff 40%,#f1f2f4 100%)}
.projects-title{left:96px;top:783px;font-size:29px;font-weight:400}
.project{left:94px;width:282px;height:55px;border-bottom:1px dotted #b9bdc1}
.project .icon{position:absolute;left:0;top:6px;width:44px;height:44px}
.project p{position:absolute;left:55px;top:6px;font-size:14.4px;font-weight:700;line-height:19px;color:var(--grey)}
.headline{left:449px;top:780px;font-size:29px;line-height:35px;font-weight:400;color:#3b3f44}
.headline strong{font-weight:400;color:var(--ink)}
.lead{left:449px;top:864px;font-size:14.4px;font-weight:700;color:var(--grey)}
.body-copy{left:449px;top:889px;width:622px;font-size:14px;line-height:19px;color:var(--grey-text)}
.step{top:961px;width:308px;height:82px;background:#fff;border:1px solid var(--line);border-radius:8px;display:flex;align-items:center}
.step .num{width:122px;padding-left:6px;font-size:66px;font-weight:700;color:#f7a6a4;letter-spacing:-2px}
.step .num span{color:var(--red)}
.step p{font-size:14.4px;font-weight:700;line-height:19px;color:var(--ink)}
.rss{left:948px;top:1055px;width:124px;height:28px;border:1px solid #cfd2d5;border-radius:5px;background:linear-gradient(#fff,#e6e8ea);display:flex;align-items:center;justify-content:center;gap:8px;font-size:14px;font-weight:700}
.footer{left:0;top:1154px;width:1176px;height:46px;background:linear-gradient(var(--red-light),var(--red) 60%,var(--red-dark));display:flex;align-items:center;justify-content:center;font-size:14px;font-weight:700;color:var(--ink)}
</style>
</head>
<body>
<div class="page">

  <div class="brand abs"><div class="brand-mark"></div><div class="brand-name">Corvan Lk</div></div>

  <nav class="nav">
    <a class="btn current" style="left:379px">Home</a>
    <a class="btn" style="left:528px">Company</a>
    <a class="btn" style="left:677px">Services</a>
    <a class="btn" style="left:826px">Solutions</a>
    <a class="btn" style="left:974px">Contacts</a>
  </nav>

  <section class="hero abs" role="img" aria-label="Photo of a smiling woman with a laptop in a server room">
    <div class="bubble red">Innovative<br>IT Solutions</div>
    <div class="bubble dark sec">Security</div>
    <div class="bubble dark rel">Unsurpassed<br>Reliability</div>
  </section>

  <article class="feature abs" style="left:59px">
    <div class="feature-art" role="img" aria-label="Faded photo of network cabling">
      <h2 style="top:14px">Perth's Safe, Secure &amp;<br>Reliable Data Centre</h2>
      <p style="top:60px">Talk to us about designing a solution to meet your needs.</p>
      <a class="btn">Read more</a>
    </div>
  </article>
  <article class="feature abs" style="left:414px">
    <div class="feature-art" role="img" aria-label="Faded illustration of a facility floor plan">
      <h2 style="top:24px">Modern Facility</h2>
      <p style="top:60px">Praesent vestibulum molestie Fusce suscipit varius. Cum sociis natoque penatibus et magnis dis parturient</p>
      <a class="btn">Read more</a>
    </div>
  </article>
  <article class="feature abs" style="left:769px">
    <div class="feature-art" role="img" aria-label="Faded photo of server racks">
      <h2 style="top:24px">Striking Results</h2>
      <p style="top:60px">Corvan Lk partners with Australia's leading providers of IT solutions and infrastructure.</p>
      <a class="btn">Read more</a>
    </div>
  </article>

  <div class="panel abs"></div>
  <div class="panel-main abs"></div>

  <h3 class="projects-title abs">Featured projects</h3>
  <div class="project abs" style="top:823px">
    <svg class="icon" viewBox="0 0 44 44"><circle cx="22" cy="22" r="21" fill="#e8201f"/><circle cx="22" cy="14" r="5" fill="#fff"/><path d="M14 34v-9a5 5 0 0 1 5-5h6a5 5 0 0 1 5 5v9z" fill="#fff"/></svg>
    <p>Praesent vestibulum molestie<br>Fusce suscipit varius.</p>
  </div>
  <div class="project abs" style="top:879px">
    <svg class="icon" viewBox="0 0 44 44"><circle cx="22" cy="22" r="21" fill="#e8201f"/><path d="M12 22l7 7 13-14" stroke="#fff" stroke-width="5" fill="none" stroke-linecap="round"/></svg>
    <p>Cum sociis natoque penatibus et<br>magnis dis parturient montes.</p>
  </div>
  <div class="project abs" style="top:933px">
    <svg class="icon" viewBox="0 0 44 44"><circle cx="22" cy="22" r="21" fill="#e8201f"/><rect x="19" y="9" width="6" height="17" rx="3" fill="#fff"/><circle cx="22" cy="33" r="3.5" fill="#fff"/></svg>
    <p>Nulla duiusce feugiat malesuada<br>odi moorbi nunc odio gravida at</p>
  </div>
  <div class="project abs" style="top:985px">
    <svg class="icon" viewBox="0 0 44 44"><circle cx="22" cy="22" r="21" fill="#e8201f"/><circle cx="22" cy="19" r="9" fill="#fff"/><rect x="18" y="27" width="8" height="7" rx="2" fill="#fff"/></svg>
    <p>Praesent vestibulum molestie<br>Fusce suscipit varius.</p>
  </div>
  <a class="btn" style="left:252px;top:1055px;width:124px;height:27px">All projects</a>

  <h1 class="headline abs">Our work is <strong>DEDICATED TO THE PROSPERITY</strong><br>of our clients!</h1>
  <p class="lead abs">Praesent vestibulum molestie Fusce suscipit varius. Cum sociis natoque penatibus et.</p>
  <p class="body-copy abs">Nulla dui.usce feugiat malesuada odio. Morbi nunc odio, gravida at, cursus nec, luctus a, lorem. Maecenas tristique orci ac sem. Duis ultricies pharetra magna. Donec accumsan male-suada orci. Donec sit amet eros.</p>

  <div class="step abs" style="left:449px"><div class="num">01<span>.</span></div><p>Praesent vestibulum<br>molestie Fusce suscipit<br>varius. Cum sociis</p></div>
  <div class="step abs" style="left:764px"><div class="num">02<span>.</span></div><p>Praesent vestibulum<br>molestie Fusce suscipit<br>varius. Cum sociis</p></div>

  <a class="btn" style="left:818px;top:1055px;width:124px;height:27px">Read more</a>
  <a class="rss abs">RSS Feed
    <svg width="18" height="18" viewBox="0 0 18 18"><rect width="18" height="18" rx="3" fill="#f39a1c"/><circle cx="5" cy="13" r="2" fill="#fff"/><path d="M4 8a6 6 0 0 1 6 6M4 4a10 10 0 0 1 10 10" stroke="#fff" stroke-width="2" fill="none"/></svg>
  </a>

  <footer class="footer abs">Copyright © 2010 Corvan Lk</footer>
</div>
</body>
</html>
```